Business Card and Stationary Design for Solstice Land Company
Solstice Land Partners
Business Card and Stationary Design for Solstice Land Company - Real Estate
Creative Brief
Use same font as used in my logo
Tobias "TK" Kalder
Realtor
2876 Mellow Crest Lane Irvine, CA 92611
tk@TheSolsticeLP.example
www.TheSolsticeLP.example
BRE Lic: 07326159
We need the following design work done: Business Cards, Presentation Folder, Letterhead, Envelopes. We will upload our logo and the design templates from our print shop for all the above items needed in order to print correctly. Business Cards (Front & Back): 4 color both sides. Presentation Folder - (Front, Back and inside) 4 colors all sides, including business card slit inside.
We will upload pictures of sample business cards (Front and Back) that we like from competitor companies.

```html
<!DOCTYPE html>
<html lang="en">
<head>
<meta charset="utf-8">
<title>Solstice Land Partners – Business Card</title>
<link rel="stylesheet" href="https://fonts.googleapis.com/css2?family=Open+Sans:ital,wght@0,400;0,600;0,700;1,400&display=swap">
<style>
  :root {
    --backdrop: #cfcfcf;
    --card: #ffffff;
    --ink: #2f2f2f;
    --muted: #555555;
    --accent: #f07a1a;
    --name-blue: #2b6f93;
    --band: #141414;
    --rule: #d9d9d9;
  }
  * { box-sizing: border-box; margin: 0; padding: 0; }
  html, body {
    width: 1200px; height: 878px; overflow: hidden;
    background: var(--backdrop);
    font-family: "Open Sans", Arial, sans-serif;
    color: var(--ink);
  }
  .canvas { position: relative; width: 1200px; height: 878px; }
  .card {
    position: absolute; width: 540px; height: 310px;
    background: var(--card); overflow: hidden;
    box-shadow: 0 6px 18px rgba(0,0,0,.18);
  }
  .card--front { left: 60px; top: 430px; }
  .card--back { left: 600px; top: 150px; }

  .brand { display: flex; align-items: center; gap: 10px; }
  .brand__mark { width: 26px; height: 26px; background: var(--accent); flex: none; }
  .brand__name { font-weight: 700; font-size: 25px; color: var(--ink); letter-spacing: -.3px; white-space: nowrap; }
  .card--front .brand { position: absolute; left: 38px; top: 34px; }
  .card--back .brand { position: absolute; left: 0; right: 0; top: 136px; justify-content: center; }
  .card--back .brand__name { font-size: 29px; }

  .contacts { position: absolute; left: 44px; top: 104px; list-style: none; font-size: 13px; color: var(--muted); }
  .contacts li { display: flex; align-items: center; gap: 8px; line-height: 21px; white-space: nowrap; }
  .contacts svg { width: 12px; height: 12px; fill: var(--accent); flex: none; }

  .person { position: absolute; left: 318px; top: 100px; }
  .person__name { font-size: 18px; font-weight: 600; color: var(--name-blue); white-space: nowrap; }
  .person__role { font-size: 12px; font-style: italic; color: var(--accent); margin-top: 2px; }

  .address { position: absolute; left: 318px; top: 172px; font-size: 13px; color: var(--muted); line-height: 19px; white-space: nowrap; }
  .licence { position: absolute; left: 318px; top: 216px; font-size: 11px; color: var(--muted); white-space: nowrap; }

  .swoosh { position: absolute; left: 0; top: 0; width: 540px; height: 310px; }
</style>
</head>
<body>
<main class="canvas">
  <section class="card card--back" aria-label="Card back">
    <div class="brand">
      <span class="brand__mark"></span>
      <span class="brand__name">Solstice Land Partners</span>
    </div>
  </section>

  <section class="card card--front" aria-label="Card front">
    <svg class="swoosh" viewBox="0 0 540 310" aria-hidden="true">
      <path d="M0 262 Q170 268 300 310 L0 310 Z" fill="var(--band)"/>
      <path d="M0 246 Q260 252 540 300" fill="none" stroke="var(--accent)" stroke-width="4"/>
      <path d="M0 236 Q280 238 540 290" fill="none" stroke="var(--rule)" stroke-width="1.5"/>
    </svg>

    <div class="brand">
      <span class="brand__mark"></span>
      <span class="brand__name">Solstice Land Partners</span>
    </div>

    <ul class="contacts">
      <li><svg viewBox="0 0 24 24"><path d="M6.6 10.8a15.1 15.1 0 0 0 6.6 6.6l2.2-2.2c.3-.3.7-.4 1-.2 1.1.4 2.3.6 3.6.6.6 0 1 .4 1 1V20c0 .6-.4 1-1 1A17 17 0 0 1 3 4c0-.6.4-1 1-1h3.5c.6 0 1 .4 1 1 0 1.3.2 2.5.6 3.6.1.3 0 .7-.2 1z"/></svg>555 014 2280</li>
      <li><svg viewBox="0 0 24 24"><path d="M2 5h20v14H2z"/></svg>tk@TheSolsticeLP.example</li>
      <li><svg viewBox="0 0 24 24"><circle cx="12" cy="12" r="10"/></svg>www.TheSolsticeLP.example</li>
    </ul>

    <div class="person">
      <p class="person__name">Tobias "TK" Kalder</p>
      <p class="person__role">Realtor</p>
    </div>

    <p class="address">2876 Mellow Crest Lane<br>Irvine, CA 92611</p>
    <p class="licence">BRE Lic: 07326159</p>
  </section>
</main>
</body>
</html>
```